E-mail Ad Design Project

I would like a lower banner ad designed for placement within an e-mail. The size has to be 450px x 230px (6in x 3.07in) and must be either a GIF or JPEG, not to exceed 30K.

We are a medical billing company that provides services to physical therapy practices in Florida, and this ad is intended for owners and office managers of physical therapy businesses. We provide therapy offices with practice management software, submit medical claims on behalf of their patients, follow-up with insurance companies on outstanding claims, and also perform necessary back-end collections with patient balances. We also are able to interface with popular therapy documentation products to streamline data entry.

The design colors should incorporate our logo and red/blue colors (see www.clinicianharbor.net).

Target Market(s)

Physical therapists and administrators of physical therapy offices

Industry/Entity Type

Physical Therapy

Requirements
Must have
• Grabbing/heading text:

Tired of Denials and Confusing Rejection Codes?
We Take the Pain Out of Medical Billing.

Offer:

Get Started Today with 2 Free Months of Billing
Nice to have
• We provide services mainly to Florida therapists, so it would be nice to have an image or text that highlights this fact. Also, the e-mail campaign this is a part of will be sent to Florida recipients.

```html
<!DOCTYPE html>
<html lang="en">
<head>
<meta charset="utf-8">
<title>Medical Billing Email Banner – Variations</title>
<link rel="stylesheet" href="https://fonts.googleapis.com/css2?family=Bowlby+One+SC&family=Open+Sans:wght@400;600&family=Roboto+Condensed:wght@700&display=swap">
<style>
  :root {
    --board: #1c1c1c;
    --board-edge: #0c0c0c;
    --blue-light: #4fb4e6;
    --blue-mid: #2a8fd0;
    --blue-deep: #1565a8;
    --white: #ffffff;
    --yellow: #ffe23a;
    --shadow-dark: #0d2f52;
    --burst-light: #ffb36b;
    --burst-deep: #f26a1b;
    --burst-text: #3a1a05;
    --photo-a: #c9c3bb;
    --photo-b: #7c8a9a;
    --photo-c: #2f4f8a;
  }
  * { box-sizing: border-box; margin: 0; padding: 0; }
  html, body { width: 1200px; height: 676px; overflow: hidden; }
  body {
    background: radial-gradient(ellipse at center, var(--board) 0%, var(--board-edge) 100%);
    position: relative;
  }
  .banner-frame {
    position: absolute;
    width: 540px;
    height: 276px;
  }
  .banner-frame--tl { left: 34px; top: 60px; }
  .banner-frame--tr { left: 602px; top: 60px; }
  .banner-frame--bl { left: 34px; top: 362px; }
  .banner-frame--br { left: 602px; top: 362px; }

  .banner {
    position: absolute;
    left: 0; top: 0;
    width: 450px;
    height: 230px;
    transform: scale(1.2);
    transform-origin: 0 0;
    overflow: hidden;
    background: linear-gradient(180deg, var(--blue-light) 0%, var(--blue-mid) 55%, var(--blue-deep) 100%);
    box-shadow: 0 2px 6px rgba(0,0,0,0.6);
  }
  .banner__photo {
    position: absolute;
    left: 0; top: 0;
    width: 450px; height: 230px;
  }
  .banner__headline {
    position: absolute;
    left: 10px; top: 14px;
    font-family: "Bowlby One SC", sans-serif;
    font-size: 22.5px;
    line-height: 33px;
    letter-spacing: 0.4px;
    color: var(--white);
    text-shadow: 1px 1px 0 var(--shadow-dark), 2px 2px 0 var(--shadow-dark), 3px 3px 2px rgba(0,0,0,0.5);
    white-space: nowrap;
  }
  .banner__headline--flat { text-shadow: 1px 1px 1px rgba(0,0,0,0.35); }
  .banner__headline--yellow { color: var(--yellow); }
  .banner__tagline {
    position: absolute;
    left: 12px; top: 122px;
    font-family: "Open Sans", sans-serif;
    font-size: 16.5px;
    line-height: 24px;
    color: var(--white);
  }
  .banner__phone {
    position: absolute;
    left: 11px; top: 178px;
    font-family: "Roboto Condensed", sans-serif;
    font-weight: 700;
    font-size: 31px;
    letter-spacing: 0.3px;
    color: var(--white);
    text-shadow: 1px 1px 0 var(--shadow-dark), 2px 2px 2px rgba(0,0,0,0.5);
  }
  .banner__phone--yellow { color: var(--yellow); }
  .offer-burst {
    position: absolute;
    left: 212px; top: 110px;
    width: 106px; height: 106px;
  }
  .offer-burst__text {
    position: absolute;
    inset: 0;
    display: flex;
    flex-direction: column;
    align-items: center;
    justify-content: center;
    font-family: "Open Sans", sans-serif;
    color: var(--burst-text);
    text-align: center;
    line-height: 1.05;
  }
  .offer-burst__small { font-size: 9px; font-weight: 600; }
  .offer-burst__big { font-family: "Roboto Condensed", sans-serif; font-size: 19px; font-weight: 700; }
  .offer-burst__mid { font-family: "Roboto Condensed", sans-serif; font-size: 13px; font-weight: 700; }
</style>
</head>
<body>

<!-- Reusable shapes -->
<svg width="0" height="0" style="position:absolute">
  <defs>
    <linearGradient id="photoFill" x1="0" y1="0" x2="1" y2="1">
      <stop offset="0" stop-color="#c9c3bb"/>
      <stop offset="0.55" stop-color="#7c8a9a"/>
      <stop offset="1" stop-color="#2f4f8a"/>
    </linearGradient>
    <radialGradient id="burstFill" cx="0.5" cy="0.45" r="0.6">
      <stop offset="0" stop-color="#ffb36b"/>
      <stop offset="1" stop-color="#f26a1b"/>
    </radialGradient>
    <symbol id="photoPanel" viewBox="0 0 450 230">
      <path d="M305 0 Q282 120 345 230 L450 230 L450 0 Z" fill="url(#photoFill)"/>
      <path d="M305 0 Q282 120 345 230" fill="none" stroke="#ffffff" stroke-width="3" opacity="0.85"/>
      <path d="M292 0 Q268 120 330 230" fill="none" stroke="#8fd3f5" stroke-width="1.5" opacity="0.6"/>
    </symbol>
    <symbol id="burst" viewBox="0 0 100 100">
      <polygon fill="url(#burstFill)" stroke="#d95510" stroke-width="0.8"
        points="50,2 56,14 67,5 69,18 82,13 79,26 93,26 86,38 98,44 87,52 97,62 84,66 90,79 76,79 77,93 65,87 59,99 50,90 41,99 35,87 23,93 24,79 10,79 16,66 3,62 13,52 2,44 14,38 7,26 21,26 18,13 31,18 33,5 44,14"/>
    </symbol>
  </defs>
</svg>

<div class="banner-frame banner-frame--tl">
  <div class="banner">
    <svg class="banner__photo" role="img" aria-label="Photo: physical therapist helping a seated patient stretch in a clinic"><use href="#photoPanel"/></svg>
    <div class="banner__headline">TIRED OF DENIALS<br>AND CONFUSING<br>REJECTION CODES?</div>
    <div class="banner__tagline">We Take the Pain Out<br>of Medical Billing.</div>
    <div class="banner__phone">866-555-0142</div>
    <div class="offer-burst">
      <svg width="106" height="106"><use href="#burst"/></svg>
      <div class="offer-burst__text">
        <span class="offer-burst__small">GET STARTED<br>TODAY WITH</span>
        <span class="offer-burst__big">2 FREE</span>
        <span class="offer-burst__mid">MONTHS</span>
        <span class="offer-burst__small">OF BILLING</span>
      </div>
    </div>
  </div>
</div>

<div class="banner-frame banner-frame--tr">
  <div class="banner">
    <svg class="banner__photo" role="img" aria-label="Photo: physical therapist helping a seated patient stretch in a clinic"><use href="#photoPanel"/></svg>
    <div class="banner__headline banner__headline--flat">TIRED OF DENIALS<br>AND CONFUSING<br>REJECTION CODES?</div>
    <div class="banner__tagline">We Take the Pain Out<br>of Medical Billing.</div>
    <div class="banner__phone">866-555-0142</div>
    <div class="offer-burst">
      <svg width="106" height="106"><use href="#burst"/></svg>
      <div class="offer-burst__text">
        <span class="offer-burst__small">GET STARTED<br>TODAY WITH</span>
        <span class="offer-burst__big">2 FREE</span>
        <span class="offer-burst__mid">MONTHS</span>
        <span class="offer-burst__small">OF BILLING</span>
      </div>
    </div>
  </div>
</div>

<div class="banner-frame banner-frame--bl">
  <div class="banner">
    <svg class="banner__photo" role="img" aria-label="Photo: physical therapist helping a seated patient stretch in a clinic"><use href="#photoPanel"/></svg>
    <div class="banner__headline">TIRED OF DENIALS<br>AND CONFUSING<br>REJECTION CODES?</div>
    <div class="banner__tagline">We Take the Pain Out<br>of Medical Billing.</div>
    <div class="banner__phone banner__phone--yellow">866-555-0142</div>
    <div class="offer-burst">
      <svg width="106" height="106"><use href="#burst"/></svg>
      <div class="offer-burst__text">
        <span class="offer-burst__small">GET STARTED<br>TODAY WITH</span>
        <span class="offer-burst__big">2 FREE</span>
        <span class="offer-burst__mid">MONTHS</span>
        <span class="offer-burst__small">OF BILLING</span>
      </div>
    </div>
  </div>
</div>

<div class="banner-frame banner-frame--br">
  <div class="banner">
    <svg class="banner__photo" role="img" aria-label="Photo: physical therapist helping a seated patient stretch in a clinic"><use href="#photoPanel"/></svg>
    <div class="banner__headline banner__headline--yellow">TIRED OF DENIALS<br>AND CONFUSING<br>REJECTION CODES?</div>
    <div class="banner__tagline">We Take the Pain Out<br>of Medical Billing.</div>
    <div class="banner__phone">866-555-0142</div>
    <div class="offer-burst">
      <svg width="106" height="106"><use href="#burst"/></svg>
      <div class="offer-burst__text">
        <span class="offer-burst__small">GET STARTED<br>TODAY WITH</span>
        <span class="offer-burst__big">2 FREE</span>
        <span class="offer-burst__mid">MONTHS</span>
        <span class="offer-burst__small">OF BILLING</span>
      </div>
    </div>
  </div>
</div>

</body>
</html>
```